Mobile Interface Design

Take an existing website design and create a Mobile interface that is creative and easy to navigate. Background programming and stuff already accomplished... need a Graphic Designer with Mobile UI expertise. Need it done quickly in 1-2 weeks.
Go to http://demo.fairwaypulse-example.com. Signup using invitation code "milvantour" - we need the pick players screen designed for a mobile platform. We have some ideas regarding the layout of the screen. I will upload a mockup. We need to stick to current design site as much as possible but also provide a better mobile site experience.
Notes of the attached file:
The header will have Teebeacon logo, Messages icon, Points and menu (lines).
Ignore second bar
Tournament Info will be a scroll down box (mobile expand layer)
Tokens bar will have the tokens from the web page 100/40
The field - will be the players from the website - will show rank, photo, name, token value (20) and a check box - to select. the check box will change the color of the layer. At the top - the filters will be similar to filters on website. There will be a clear/show selected button to filter list (not required to show on design) - at bottom "Next Choose Winner" button.
We need footer with menu links "Pick Players", "My Compass", My Games", "My Profile".
If you have any specific questions, please let me know before starting on it.
Updates
This is not a contest for everyone looking to work on it. If you submit your portfolio and ideas, we will work with them directly on the design/delivery. This is my first time posting a project and didn't realize I created a contest.
Target Market(s)
iOS and Android
Look and feel
Each slider illustrates characteristics of the customer's brand and the style your logo design should communicate.

```html
<!DOCTYPE html>
<html lang="en">
<head>
<meta charset="utf-8">
<title>Teebeacon – Pick Players</title>
<link rel="stylesheet" href="https://fonts.googleapis.com/css2?family=Open+Sans:wght@400;600;700&display=swap">
<style>
:root{
  --stage:#5b5b5b;
  --status:#000000;
  --header-top:#3a4e78;
  --header-bottom:#0f1e40;
  --chip:#17233f;
  --chip-edge:#5f6f95;
  --pts:#3fb6ff;
  --bar-light:#eef0f4;
  --bar-mid:#d7dae1;
  --ink:#1d2740;
  --ink-soft:#33394a;
  --field-top:#2c3447;
  --field-bottom:#0d1424;
  --row-top:#f4f5f8;
  --row-bottom:#c6c9d2;
  --arrow-top:#3e4d75;
  --arrow-bottom:#18223f;
  --token-dark:#6d6f74;
  --token-light:#e9eaec;
  --action-top:#4d7cff;
  --action-bottom:#1d48d8;
  --footer:#e3e4e8;
  --foot-btn:#85888f;
  --social-a:#3b5a9a;
  --social-b:#2ea7dc;
  --social-c:#1c77b5;
  --photo-a:#8a8f98;
  --photo-b:#d2c3b1;
}
*{box-sizing:border-box;margin:0;padding:0}
html,body{width:706px;height:1200px;overflow:hidden}
body{background:var(--stage);font-family:"Open Sans",Arial,sans-serif;color:var(--ink)}
.screen{position:absolute;left:0;top:68px;width:706px;height:1064px;background:#fff;overflow:hidden;display:flex;flex-direction:column}

.status-bar{height:20px;background:var(--status);color:#fff;font-size:11px;display:flex;align-items:center;justify-content:space-between;padding:0 10px}

.app-header{height:87px;background:linear-gradient(var(--header-top),var(--header-bottom));display:flex;align-items:center;padding:0 14px 0 25px}
.brand{font-size:28px;font-weight:400;color:#fff;letter-spacing:-.5px;display:flex;align-items:center;gap:8px}
.brand-dot{width:8px;height:8px;border-radius:50%;background:#fff}
.header-actions{margin-left:auto;display:flex;gap:13px}
.chip{height:39px;border-radius:7px;background:var(--chip);border:1px solid var(--chip-edge);color:#fff;font-size:13px;display:flex;align-items:center;justify-content:center;gap:8px}
.chip-mail{width:72px}
.chip-pts{width:75px}
.chip-pts b{color:var(--pts);font-weight:400}
.chip-menu{width:125px;background:linear-gradient(#ffffff,#c9ccd4);color:var(--ink);border-color:#9aa0ad}
.mail-icon{width:26px;height:18px;background:#dfe2e8;border-radius:2px}

.tournament-info{height:46px;background:linear-gradient(var(--bar-light),var(--bar-mid));display:flex;align-items:center;padding:0 20px 0 20px;font-size:16px;color:var(--ink-soft);border-bottom:1px solid #b8bcc6}
.tournament-info svg{margin-left:auto}

.tokens-bar{height:66px;background:linear-gradient(#ffffff,#e6e7eb);display:flex;align-items:center;padding-left:125px}
.tokens-label{font-size:20px;color:var(--ink-soft);margin-right:14px}
.token-box{display:flex;width:487px;height:50px;border:1px solid #8c8e93}
.token{display:flex;align-items:center;font-family:Arial,sans-serif;font-weight:700;font-size:15px;line-height:1.15}
.token-primary{width:226px;background:linear-gradient(#85878c,var(--token-dark));color:#fff;justify-content:center;gap:22px;text-align:center}
.token-backup{flex:1;background:linear-gradient(#fbfbfc,var(--token-light));color:#7b7d82;padding-left:18px;gap:12px}

.field-bar{height:55px;background:linear-gradient(var(--field-top),var(--field-bottom));display:flex;align-items:center;padding-left:32px}
.field-tab{width:172px;height:36px;border-radius:6px;background:linear-gradient(#1c2f5e,#0a1530);border:1px solid #4d5c82;color:#fff;font-size:18px;display:flex;align-items:center;justify-content:center}
.filters-label{color:#fff;font-size:18px;margin-left:45px}
.sort-select{margin-left:18px;width:205px;height:28px;background:#fff;border-radius:3px;display:flex;align-items:center;font-size:14px;color:#8a8d94;padding-left:14px;position:relative}
.sort-select span.caret{position:absolute;right:0;top:0;width:24px;height:28px;background:#6d7079;border-radius:0 3px 3px 0;display:flex;align-items:center;justify-content:center}

.player-list{list-style:none}
.player{height:74px;background:linear-gradient(var(--row-top),var(--row-bottom));border-bottom:1px solid #a7abb5;display:flex;align-items:center;position:relative}
.player-photo{position:absolute;left:15px;top:4px;width:72px;height:66px;background:linear-gradient(135deg,var(--photo-b),var(--photo-a))}
.player-name{position:absolute;left:108px;top:13px;font-size:17px;color:var(--ink)}
.player-rank{position:absolute;left:108px;top:39px;font-size:12px;color:var(--ink-soft)}
.flag{position:absolute;left:252px;top:14px;width:25px;height:25px;border-radius:50%;border:1px solid #b9bcc4}
.flag-us{background:linear-gradient(#c8323a 0 50%,#e9ecf2 50% 100%)}
.flag-uk{background:radial-gradient(circle,#d3282f 0 30%,#1c3b86 31%)}
.flag-au{background:radial-gradient(circle at 35% 35%,#e9ecf2 0 14%,#1d3a8a 15%)}
.stats-btn{position:absolute;left:284px;top:29px;width:127px;height:28px;border-radius:5px;background:linear-gradient(#ffffff,#e0e2e7);border:1px solid #a2a6b0;font-size:12px;color:var(--ink-soft);display:flex;align-items:center;justify-content:center}
.open-btn{position:absolute;left:617px;top:10px;width:72px;height:53px;border-radius:5px;background:linear-gradient(var(--arrow-top),var(--arrow-bottom));display:flex;align-items:center;justify-content:center}

.action-bar{height:72px;background:linear-gradient(#1c2440,#050a18);display:flex;align-items:center;justify-content:flex-end;padding-right:17px}
.next-btn{width:219px;height:50px;border-radius:6px;background:linear-gradient(var(--action-top),var(--action-bottom));border:1px solid #7c9cff;color:#fff;font-size:18px;display:flex;align-items:center;justify-content:center}

.app-footer{flex:1;background:var(--footer);display:flex;align-items:center;padding:0 10px 0 21px;border-top:1px solid #fff}
.foot-nav{display:flex;gap:12px}
.foot-link{width:110px;height:25px;border-radius:12px;background:linear-gradient(#9c9fa6,var(--foot-btn));color:#fff;font-size:11px;display:flex;align-items:center;justify-content:center}
.follow{margin-left:auto;display:flex;align-items:center;gap:4px;font-size:11px;color:var(--ink-soft)}
.follow i{width:21px;height:21px;border-radius:3px;display:block}
.follow i:nth-of-type(1){background:var(--social-a);margin-left:4px}
.follow i:nth-of-type(2){background:var(--social-b)}
.follow i:nth-of-type(3){background:var(--social-c)}
</style>
</head>
<body>
<main class="screen">
  <div class="status-bar"><span>Tablet</span><span>4:20 AM</span><span>32%</span></div>

  <header class="app-header">
    <div class="brand"><span>Teebeacon</span><span class="brand-dot"></span></div>
    <nav class="header-actions">
      <div class="chip chip-mail"><span class="mail-icon"></span>Mail</div>
      <div class="chip chip-pts"><b>3420</b>pts</div>
      <div class="chip chip-menu">
        <svg width="30" height="20" viewBox="0 0 30 20"><g stroke="#1d2740" stroke-width="3"><line x1="2" y1="4" x2="18" y2="4"/><line x1="8" y1="10" x2="28" y2="10"/><line x1="2" y1="16" x2="22" y2="16"/></g></svg>
        Menus
        <svg width="20" height="20" viewBox="0 0 20 20"><circle cx="10" cy="10" r="9" fill="#3c7be0"/><path d="M5.5 8l4.5 4.5L14.5 8" fill="none" stroke="#fff" stroke-width="2"/></svg>
      </div>
    </nav>
  </header>

  <div class="tournament-info">Tournament Info
    <svg width="16" height="12" viewBox="0 0 16 12"><path d="M0 0h16L8 12z" fill="#1d2740"/></svg>
  </div>

  <div class="tokens-bar">
    <span class="tokens-label">Tokens</span>
    <div class="token-box">
      <div class="token token-primary"><span>100<br>Player Tokens</span>
        <svg width="26" height="12" viewBox="0 0 26 12"><path d="M0 6h20M15 1l6 5-6 5" fill="none" stroke="#fff" stroke-width="3"/></svg></div>
      <div class="token token-backup"><span>40<br>Backup Player Tokens</span>
        <svg width="26" height="12" viewBox="0 0 26 12"><path d="M0 6h20M15 1l6 5-6 5" fill="none" stroke="#8a8c91" stroke-width="3"/></svg></div>
    </div>
  </div>

  <div class="field-bar">
    <div class="field-tab">Field</div>
    <span class="filters-label">Filters</span>
    <div class="sort-select">Sort/Filter By<span class="caret"><svg width="10" height="8" viewBox="0 0 10 8"><path d="M0 0h10L5 8z" fill="#fff"/></svg></span></div>
  </div>

  <ul class="player-list">
    <li class="player"><div class="player-photo" role="img" aria-label="Player portrait photo"></div><span class="player-name">Dorian Valcourt</span><span class="player-rank">World Ranking : 42</span><span class="flag flag-us" role="img" aria-label="United States flag"></span><span class="stats-btn">Players Statistics</span><span class="open-btn"><svg width="14" height="18" viewBox="0 0 14 18"><path d="M3 2l7 7-7 7" fill="none" stroke="#fff" stroke-width="3"/></svg></span></li>
    <li class="player"><div class="player-photo" role="img" aria-label="Player portrait photo"></div><span class="player-name">Dorian Valcourt</span><span class="player-rank">World Ranking : 42</span><span class="flag flag-uk" role="img" aria-label="United Kingdom flag"></span><span class="stats-btn">Players Statistics</span><span class="open-btn"><svg width="14" height="18" viewBox="0 0 14 18"><path d="M3 2l7 7-7 7" fill="none" stroke="#fff" stroke-width="3"/></svg></span></li>
    <li class="player"><div class="player-photo" role="img" aria-label="Player swinging a golf club"></div><span class="player-name">Dorian Valcourt</span><span class="player-rank">World Ranking : 42</span><span class="flag flag-au" role="img" aria-label="Australia flag"></span><span class="stats-btn">Players Statistics</span><span class="open-btn"><svg width="14" height="18" viewBox="0 0 14 18"><path d="M3 2l7 7-7 7" fill="none" stroke="#fff" stroke-width="3"/></svg></span></li>
    <li class="player"><div class="player-photo" role="img" aria-label="Player portrait photo"></div><span class="player-name">Dorian Valcourt</span><span class="player-rank">World Ranking : 42</span><span class="flag flag-us" role="img" aria-label="United States flag"></span><span class="stats-btn">Players Statistics</span><span class="open-btn"><svg width="14" height="18" viewBox="0 0 14 18"><path d="M3 2l7 7-7 7" fill="none" stroke="#fff" stroke-width="3"/></svg></span></li>
    <li class="player"><div class="player-photo" role="img" aria-label="Player seated outdoors"></div><span class="player-name">Dorian Valcourt</span><span class="player-rank">World Ranking : 42</span><span class="flag flag-uk" role="img" aria-label="United Kingdom flag"></span><span class="stats-btn">Players Statistics</span><span class="open-btn"><svg width="14" height="18" viewBox="0 0 14 18"><path d="M3 2l7 7-7 7" fill="none" stroke="#fff" stroke-width="3"/></svg></span></li>
    <li class="player"><div class="player-photo" role="img" aria-label="Player portrait photo"></div><span class="player-name">Dorian Valcourt</span><span class="player-rank">World Ranking : 42</span><span class="flag flag-au" role="img" aria-label="Australia flag"></span><span class="stats-btn">Players Statistics</span><span class="open-btn"><svg width="14" height="18" viewBox="0 0 14 18"><path d="M3 2l7 7-7 7" fill="none" stroke="#fff" stroke-width="3"/></svg></span></li>
    <li class="player"><div class="player-photo" role="img" aria-label="Player portrait photo"></div><span class="player-name">Dorian Valcourt</span><span class="player-rank">World Ranking : 42</span><span class="flag flag-us" role="img" aria-label="United States flag"></span><span class="stats-btn">Players Statistics</span><span class="open-btn"><svg width="14" height="18" viewBox="0 0 14 18"><path d="M3 2l7 7-7 7" fill="none" stroke="#fff" stroke-width="3"/></svg></span></li>
    <li class="player"><div class="player-photo" role="img" aria-label="Player portrait photo"></div><span class="player-name">Dorian Valcourt</span><span class="player-rank">World Ranking : 42</span><span class="flag flag-uk" role="img" aria-label="United Kingdom flag"></span><span class="stats-btn">Players Statistics</span><span class="open-btn"><svg width="14" height="18" viewBox="0 0 14 18"><path d="M3 2l7 7-7 7" fill="none" stroke="#fff" stroke-width="3"/></svg></span></li>
    <li class="player"><div class="player-photo" role="img" aria-label="Player portrait photo"></div><span class="player-name">Dorian Valcourt</span><span class="player-rank">World Ranking : 42</span><span class="flag flag-au" role="img" aria-label="Australia flag"></span><span class="stats-btn">Players Statistics</span><span class="open-btn"><svg width="14" height="18" viewBox="0 0 14 18"><path d="M3 2l7 7-7 7" fill="none" stroke="#fff" stroke-width="3"/></svg></span></li>
  </ul>

  <div class="action-bar"><div class="next-btn">Next Choose Winner</div></div>

  <footer class="app-footer">
    <nav class="foot-nav">
      <span class="foot-link">Pick Players</span>
      <span class="foot-link">My Compass</span>
      <span class="foot-link">My Games</span>
      <span class="foot-link">My Profile</span>
    </nav>
    <div class="follow">Follow us :<i></i><i></i><i></i></div>
  </footer>
</main>
</body>
</html>
```